Brightwell cleaning and maintenance company

An expansive website whereby we can advertise our commercial cleaning and maintenance services across a service portfolio of commercial cleaning and property maintenance. Whereby potential skilled resources can deposit there resume so we can collaborate and match candidates to a broad range of cleaning and maintenance jobs/projects.
Updates

Looking for more extensive ideas so the front page can change pictures on it with the focus for Brightwell Commercial Cleaning and Maintenance. Also need to bring in all the portfolios we offer including 1. Equipment Cleaning and Sanitisation Services 2. High pressure gurney and play ground equipment cleaning 3. General Cleaning and Property Facilities Management 4. Project and Recruiting Services, to allow for potential professional cleaners, handy man, mechanics, warehousing resources , electricians to deposit there resume. Most of the designers have stuck with the old portfolio categories , however the portfolio of services we offer has been updated so that needs to be reflected in the website. Also not necessary to use all my original photos I would like the opening page of the website to perhaps be able to change and have different pictures is that possible thank you

```html
<!DOCTYPE html>
<html lang="en">
<head>
<meta charset="utf-8">
<title>Brightwell — Commercial Cleaning &amp; Maintenance</title>
<link href="https://fonts.googleapis.com/css2?family=Poppins:wght@400;500;600;700&family=Roboto:wght@300;400&family=Roboto+Condensed:wght@700&display=swap" rel="stylesheet">
<style>
:root{
  --orange:#ec5512;
  --orange-soft:rgba(236,85,18,.88);
  --navy:#1f3d75;
  --navy-deep:#173a73;
  --text-blue:#1d4e94;
  --grey-band:#ebebeb;
  --footer:#2b2b2b;
  --footer-text:#bfbfbf;
  --white:#fff;
}
*{margin:0;padding:0;box-sizing:border-box}
html,body{width:1200px;height:3343px;overflow:hidden;background:var(--white)}
body{font-family:'Roboto',sans-serif;color:var(--text-blue);position:relative}
.wrap{width:730px;margin:0 auto;position:relative}
.brand{color:var(--orange);font-family:'Poppins',sans-serif;font-weight:500}

/* header */
.topbar{height:115px;border-bottom:3px solid var(--navy);position:relative}
.logo{position:absolute;left:236px;top:32px;display:flex;align-items:center;gap:10px}
.logo-dot{width:42px;height:42px;border-radius:50%;background:var(--navy)}
.logo-name{font-family:'Poppins',sans-serif;font-weight:500;font-size:32px;color:var(--orange)}
.hours{position:absolute;left:540px;top:46px;display:flex;gap:10px;font-family:'Poppins',sans-serif;font-size:11px;color:var(--navy);line-height:15px}
.call{position:absolute;left:698px;top:42px;font-family:'Poppins',sans-serif;color:var(--navy);text-align:right}
.call small{display:block;font-size:11px}
.call strong{font-weight:400;font-size:17px}
.quote-btn{position:absolute;left:827px;top:38px;width:140px;height:39px;border-radius:20px;background:var(--orange);color:var(--white);font-family:'Poppins',sans-serif;font-weight:600;font-size:10px;display:flex;align-items:center;justify-content:center}
.nav{height:77px;display:flex;justify-content:space-between;align-items:center;width:730px;margin:0 auto;font-family:'Poppins',sans-serif;font-weight:600;font-size:13px;color:#222}
.nav .active{color:var(--orange)}

/* hero */
.hero{height:437px;position:relative;background:linear-gradient(135deg,#c9cdd2 0%,#8c97a3 35%,#2d4f7d 60%,#3a6ca8 80%,#b9c2cc 100%)}
.hero-title{position:absolute;left:0;right:0;top:152px;text-align:center;color:var(--white);font-family:'Poppins',sans-serif;line-height:60px}
.hero-title span{display:block;font-size:50px;font-weight:400;letter-spacing:2px}
.hero-title strong{display:block;font-size:50px;font-weight:700;letter-spacing:2px}
.hero-btns{position:absolute;top:293px;left:0;right:0;display:flex;justify-content:center;gap:16px}
.hero-btns a{width:128px;height:38px;display:flex;align-items:center;justify-content:center;font-family:'Poppins',sans-serif;font-weight:600;font-size:11px;color:var(--white);text-decoration:none}
.btn-outline{border:2px solid var(--white)}
.btn-solid{background:var(--orange)}
.arrow{position:absolute;top:204px;width:32px;height:32px;background:var(--white);display:flex;align-items:center;justify-content:center}
.arrow.left{left:145px}.arrow.right{left:1034px}
.dots{position:absolute;top:387px;left:0;right:0;display:flex;justify-content:center;gap:3px}
.dots i{width:9px;height:9px;border:1px solid var(--white);border-radius:50%}
.dots i:first-child{background:var(--white)}

/* intro */
.intro{padding-top:70px}
.h-cond{font-family:'Roboto Condensed',sans-serif;font-weight:700;color:var(--navy-deep);font-size:29px;line-height:32px}
.intro-text{font-weight:300;font-size:16.5px;line-height:24px;color:var(--text-blue);text-align:justify}
.intro-text + .intro-text{margin-top:24px}
.pillars{display:flex;gap:8px;margin-top:30px;height:458px}
.pillar{flex:1;display:flex;flex-direction:column}
.pillar-top{height:127px;background:var(--orange);display:flex;align-items:center;justify-content:center}
.pillar-body{flex:1;background:var(--navy);padding:18px 14px;color:var(--white)}
.pillar-body h3{font-family:'Roboto Condensed',sans-serif;font-size:28px;line-height:32px;margin-bottom:4px;color:var(--white)}
.pillar-text{font-weight:300;font-size:15.5px;line-height:24px;letter-spacing:.2px;color:var(--white);text-align:left}
.values{margin-top:34px}
.values ul{list-style:none;font-weight:300;font-size:16.5px;line-height:25.5px}
.values li{padding-left:14px;text-indent:-14px}
.values li::before{content:"• ";}

/* portfolio */
.portfolio{position:absolute;top:1809px;left:0;width:1200px;height:779px;background:var(--grey-band)}
.sec-title{font-family:'Poppins',sans-serif;font-weight:700;font-size:25px;letter-spacing:1px;color:var(--navy-deep);text-align:center}
.portfolio .sec-title{margin-top:55px}
.tiles{position:absolute;top:134px;left:235px;width:731px;display:grid;grid-template-columns:356px 356px;gap:20px 19px}
.tile{height:272px;position:relative}
.tile-label{position:absolute;left:0;right:0;bottom:0;height:79px;background:var(--orange-soft);color:var(--white);font-family:'Poppins',sans-serif;font-weight:700;font-size:17.5px;letter-spacing:.8px;line-height:22px;text-align:center;display:flex;align-items:center;justify-content:center}

/* blog */
.blog{position:absolute;top:2588px;left:0;width:1200px;height:427px}
.blog .sec-title{margin-top:52px}
.posts{position:absolute;top:114px;left:236px;display:flex;gap:19px}
.post{width:231px;font-family:'Poppins',sans-serif}
.post-img{height:138px;position:relative}
.post-meta{position:absolute;left:8px;bottom:11px;display:flex;gap:4px}
.post-meta span{background:var(--orange);color:var(--white);font-size:8px;font-weight:600;padding:3px 6px}
.post h4{margin-top:16px;font-size:10.5px;font-weight:600;color:#222}
.post-text{margin-top:6px;font-size:8.5px;line-height:15px;color:#777}
.post a{display:block;margin-top:10px;font-size:8px;font-weight:600;color:#444;text-decoration:none}

/* footer */
.footer{position:absolute;top:3015px;left:0;width:1200px;height:328px;background:var(--footer);font-family:'Poppins',sans-serif;color:var(--footer-text)}
.f-about{position:absolute;left:236px;top:60px;width:210px}
.f-logo{display:flex;align-items:center;gap:8px}
.f-logo .logo-dot{width:32px;height:32px}
.f-logo .logo-name{font-size:24px}
.f-about-text{margin-top:14px;font-size:9px;line-height:15px}
.socials{display:flex;gap:7px;margin-top:16px}
.socials i{width:21px;height:21px;border-radius:50%;border:1px solid #666;background:#1e1e1e}
.f-col{position:absolute;top:60px}
.f-col h5{font-size:11.5px;font-weight:600;color:var(--white)}
.f-col h5::after{content:"";display:block;width:42px;height:2px;background:var(--orange);margin-top:10px}
.f-contact{left:466px}
.f-item{display:flex;gap:10px;margin-top:22px;font-size:8.5px;line-height:13px}
.f-links{left:645px}
.f-links ul{list-style:none;margin-top:16px;font-size:8.5px;line-height:22.5px}
.f-links li::before{content:"› ";color:var(--orange)}
.f-news{left:771px;width:196px}
.f-news-text{margin-top:18px;font-size:8.5px;line-height:17px}
.subscribe{margin-top:14px;height:30px;border-radius:16px;background:var(--white);display:flex;align-items:center;justify-content:space-between;padding:0 4px 0 12px;font-size:8.5px;color:#999}
.subscribe b{width:22px;height:22px;border-radius:50%;background:var(--orange);display:flex;align-items:center;justify-content:center}
.copyright{position:absolute;top:278px;left:236px;width:731px;display:flex;justify-content:space-between;font-size:8.5px;color:#888}
.copyright span+span{margin-left:18px}
</style>
</head>
<body>

<header class="topbar">
  <div class="logo"><span class="logo-dot"></span><span class="logo-name">Brightwell</span></div>
  <div class="hours">
    <svg width="18" height="18" viewBox="0 0 18 18"><circle cx="9" cy="9" r="7.5" fill="none" stroke="#ec5512" stroke-width="2"/><path d="M9 5v4.5h3" stroke="#ec5512" stroke-width="2" fill="none"/></svg>
    <div>8:00am - 5:00pm<br>Mon - Fri</div>
  </div>
  <div class="call"><small>Call us on:</small><strong>1300 555 210</strong></div>
  <div class="quote-btn">GET A QUOTE</div>
</header>

<nav class="nav">
  <span class="active">HOME</span><span>ABOUT US</span><span>OUR SERVICES</span><span>OUR PEOPLE</span><span>SAFETY &amp; COMPLIANCE</span><span>CONTACT US</span>
</nav>

<section class="hero" role="img" aria-label="Cleaner at work with a blue cleaning trolley in a washroom">
  <div class="arrow left"><svg width="10" height="10" viewBox="0 0 10 10"><path d="M6.5 1.5L3 5l3.5 3.5" stroke="#222" fill="none" stroke-width="1.4"/></svg></div>
  <div class="arrow right"><svg width="10" height="10" viewBox="0 0 10 10"><path d="M3.5 1.5L7 5l-3.5 3.5" stroke="#222" fill="none" stroke-width="1.4"/></svg></div>
  <h1 class="hero-title"><span>PLAYGROUND</span><strong>CLEANING</strong></h1>
  <div class="hero-btns"><a class="btn-outline" href="#">READ MORE</a><a class="btn-solid" href="#">CONTACT US</a></div>
  <div class="dots"><i></i><i></i><i></i><i></i></div>
</section>

<main class="wrap intro">
  <h2 class="h-cond">WORKING WITH <span class="brand">Brightwell</span></h2>
  <p class="intro-text">We are <span class="brand">Brightwell</span>, a leading Australian cleaning services company.</p>
  <p class="intro-text">When you work with <span class="brand">Brightwell</span> it is easy to do business with us. We have been in the equipment services industry for close to 15 years.</p>
  <p class="intro-text">Our people are professional, reliable and service oriented. In every interaction you have; on site, receiving help from our service support staff, or rolling-out new cleaning sites, you will see and feel the benefits of using <span class="brand">Brightwell</span>. The pride we take in our work and a prevailing focus on employees, customers and partners, delivers a consistent and superior ongoing service</p>

  <div class="pillars">
    <article class="pillar">
      <div class="pillar-top">
        <svg width="62" height="62" viewBox="0 0 62 62" fill="none" stroke="#fff" stroke-width="2.5"><circle cx="20" cy="14" r="5"/><circle cx="40" cy="10" r="5"/><circle cx="16" cy="32" r="5"/><path d="M31 22v22M20 19l11 10M40 15l-9 10M16 37l15 7"/><path d="M12 46h38l-4 10H16z"/></svg>
      </div>
      <div class="pillar-body"><h3>OUR PURPOSE</h3><p class="pillar-text">To support and extend the life of equipment, maximize product yield and achieve high quality hygiene standards for our food and equipment service clients. We deliver this by ensuring every person in our service chain delivers their work focusing on high quality and reliable cleaning standards.</p></div>
    </article>
    <article class="pillar">
      <div class="pillar-top">
        <svg width="62" height="62" viewBox="0 0 62 62" fill="#fff"><path d="M31 0l4 27 27 4-27 4-4 27-4-27-27-4 27-4z"/></svg>
      </div>
      <div class="pillar-body"><h3>OUR VISION</h3><p class="pillar-text">A sustainable food service and equipment cleaning company that creates value for customers, supports its employees in work and life and gives back to the community – now and for generations to come.</p></div>
    </article>
    <article class="pillar">
      <div class="pillar-top">
        <svg width="70" height="70" viewBox="0 0 70 70" fill="none" stroke="#fff" stroke-width="3"><circle cx="35" cy="35" r="32"/><circle cx="35" cy="35" r="22" stroke-width="1.5"/><path d="M35 35l14-14-8 18zM35 35L21 49l8-18z" fill="#fff"/></svg>
      </div>
      <div class="pillar-body"><h3>OUR STRATEGY</h3><p class="pillar-text">To differentiate ourselves through a prevailing focus on customer service, in everything we do and every interaction we have. We treat our people as skilled cleaning professionals who are the foundation of our company’s sustainability.</p></div>
    </article>
  </div>

  <section class="values">
    <h2 class="h-cond">WE VALUE</h2>
    <ul>
      <li>Safety and the Environment - We are committed to providing a safe and healthy working environment;</li>
      <li>Professionalism/Integrity - We are committed to doing what we say we are going to do;</li>
      <li>Sustainability - Achieving results that are mutually beneficial for our employees, our customers, our partners and the company;</li>
      <li>Positive Working Relationships - Having relationships that focus on shared goals and creation of value for all parties;</li>
      <li>Respect for each other - The embracing of diversity, enriched by openness, sharing, trust, teamwork and involvement.</li>
    </ul>
  </section>
</main>

<section class="portfolio">
  <h2 class="sec-title">SERVICE PORTFOLIO</h2>
  <div class="tiles">
    <div class="tile" role="img" aria-label="Blue service truck parked among trees" style="background:linear-gradient(180deg,#8fb8d8 0%,#5d7d4a 45%,#2d4f8a 75%)">
      <div class="tile-label">EQUIPMENT CLEANING AND<br>SANITISATION SERVICES</div>
    </div>
    <div class="tile" role="img" aria-label="Children playing on playground equipment under blue sky" style="background:linear-gradient(180deg,#3f8fd6 0%,#7ab4e6 35%,#c96b3c 70%)">
      <div class="tile-label">HIGH PRESSURE GURNEY AND<br>PLAY GROUND CLEANING</div>
    </div>
    <div class="tile" role="img" aria-label="Handyman working with a power tool" style="background:linear-gradient(135deg,#c9a88a 0%,#8a6a50 40%,#e0b020 70%,#444 100%)">
      <div class="tile-label">GENERAL CLEANING, PROPERTY<br>FACILITY MANAGEMENT,<br>HANDYMAN SERVICES</div>
    </div>
    <div class="tile" role="img" aria-label="Recruitment candidates waiting for interviews" style="background:linear-gradient(180deg,#e8e6e2 0%,#bdb8b0 50%,#3b4250 80%)">
      <div class="tile-label">PROJECTS AND<br>RECRUITING SERVICES</div>
    </div>
  </div>
</section>

<section class="blog">
  <h2 class="sec-title">BLOG</h2>
  <div class="posts">
    <article class="post">
      <div class="post-img" role="img" aria-label="Cleaner wiping a kitchen surface" style="background:linear-gradient(135deg,#f2f2f2,#c8c8c8 60%,#7fb33a)"><div class="post-meta"><span>03 Aug, 2018</span><span>10</span></div></div>
      <h4>LOREM IPSUM DOLOR</h4>
      <p class="post-text">Lorem ipsum dolor sit amet, consectetur adipiscing elit. Quisque iaculis elementum eleifend. Cras malesuada vitae enim id imperdiet. Vestibulum vestibulum egestas.</p>
      <a href="#">READ MORE</a>
    </article>
    <article class="post">
      <div class="post-img" role="img" aria-label="Worker pressure cleaning outdoors" style="background:linear-gradient(135deg,#e0a050,#5a4a30 55%,#2a2a22)"><div class="post-meta"><span>03 Aug, 2018</span><span>10</span></div></div>
      <h4>LOREM IPSUM DOLOR</h4>
      <p class="post-text">Lorem ipsum dolor sit amet, consectetur adipiscing elit. Quisque iaculis elementum eleifend. Cras malesuada vitae enim id imperdiet. Vestibulum vestibulum egestas.</p>
      <a href="#">READ MORE</a>
    </article>
    <article class="post">
      <div class="post-img" role="img" aria-label="Cleaner mopping a room with moving boxes" style="background:linear-gradient(135deg,#d8d4cc,#f0ede8 50%,#b89870)"><div class="post-meta"><span>03 Aug, 2018</span><span>10</span></div></div>
      <h4>LOREM IPSUM DOLOR</h4>
      <p class="post-text">Lorem ipsum dolor sit amet, consectetur adipiscing elit. Quisque iaculis elementum eleifend. Cras malesuada vitae enim id imperdiet. Vestibulum vestibulum egestas.</p>
      <a href="#">READ MORE</a>
    </article>
  </div>
</section>

<footer class="footer">
  <div class="f-about">
    <div class="f-logo"><span class="logo-dot"></span><span class="logo-name">Brightwell</span></div>
    <p class="f-about-text">We are Brightwell, a leading, Australian owned, cleaning services company. When you work with Brightwell it is easy to do business with us.</p>
    <div class="socials"><i></i><i></i><i></i></div>
  </div>
  <div class="f-col f-contact">
    <h5>CONTACT INFO</h5>
    <div class="f-item">
      <svg width="12" height="12" viewBox="0 0 12 12"><path d="M3 1l2 2.5-1.2 1.5a7 7 0 0 0 3.2 3.2L8.5 7 11 9l-1.3 2C5 10.5 1.5 7 1 2.3z" fill="none" stroke="#ec5512"/></svg>
      <div>Call Us<br>1300 555 210<br>0400 555 317</div>
    </div>
    <div class="f-item">
      <svg width="12" height="12" viewBox="0 0 12 12"><rect x="1" y="2.5" width="10" height="7" fill="none" stroke="#ec5512"/><path d="M1 2.5l5 4 5-4" fill="none" stroke="#ec5512"/></svg>
      <div>Email Us<br>hello@brightwell-services.example</div>
    </div>
  </div>
  <div class="f-col f-links">
    <h5>QUICK LINKS</h5>
    <ul><li>Home</li><li>About us</li><li>Safety &amp; Compliance</li><li>Services</li><li>Our People</li><li>Contact</li></ul>
  </div>
  <div class="f-col f-news">
    <h5>NEWSLETTER</h5>
    <p class="f-news-text">Subscribe to get updates right in your inbox. We promise to not send you spams.</p>
    <div class="subscribe"><span>✉ Enter email here</span><b><svg width="10" height="10" viewBox="0 0 10 10"><path d="M1 5l8-4-3 8-1.5-3z" fill="#fff"/></svg></b></div>
  </div>
  <div class="copyright"><span>Copyright © 2020 Brightwell. All Right Reserved.</span><div><span>Terms &amp; Condition</span><span>Privacy Policy</span></div></div>
</footer>

</body>
</html>
```